Website customization using WordPress Theme already purchased

Need informational website for Korvath Bridge LLC. Korvath Bridge is investment group company for multiple cloud based products and website. We need website for anyone coming to our website to be able get information on our products. I already have WordPress theme that I would like to use. Right person/company will be able to customize WordPress theme to our needs and be able to give us final product of 7-9 pages of complete website.

Industry/Entity Type

Investment

Number of Pages Required

5+ page

Colors
add136
3176b5
ec1f27
f37122

```html
<!DOCTYPE html>
<html lang="en">
<head>
<meta charset="utf-8">
<title>Korvath Bridge LLC</title>
<link href="https://fonts.googleapis.com/css2?family=Open+Sans:wght@300;400;600;700&display=swap" rel="stylesheet">
<style>
:root{
  --blue:#3176b5;
  --orange:#f37122;
  --green:#add136;
  --red:#ec1f27;
  --ink:#3a3a3a;
  --muted:#8a8a8a;
  --line:#e3e3e3;
  --soft:#f7f7f7;
  --hero-a:#0f2a33;
  --hero-b:#1d5560;
  --hero-c:#2f6b5a;
}
*{box-sizing:border-box;margin:0;padding:0}
html,body{width:1200px;height:2752px;overflow:hidden}
body{font-family:"Open Sans",Arial,sans-serif;color:var(--ink);background:#fff;position:relative}
.abs{position:absolute}
a{color:inherit;text-decoration:none}

/* hero */
.hero{position:absolute;left:0;top:0;width:1200px;height:606px;
  background:radial-gradient(circle at 80% 40%,var(--hero-c) 0,transparent 45%),
  radial-gradient(circle at 30% 70%,var(--hero-b) 0,transparent 55%),
  linear-gradient(180deg,#0c1f27,var(--hero-a) 60%,#143a40)}
.brand{left:97px;top:37px;display:flex;align-items:center;gap:14px;color:#fff;font-weight:700;font-size:24px}
.brand-dot{width:64px;height:64px;border-radius:50%;background:var(--blue);border:5px solid #fff}
.nav{top:62px;left:475px;display:flex;align-items:center;color:#fff;font-size:12.5px;font-weight:600;text-transform:uppercase}
.nav a{margin-right:30px}
.social{top:57px;left:1004px;display:flex;gap:7px}
.social span{width:28px;height:28px;border-radius:50%}
.hero-media{left:97px;top:220px;width:641px;height:261px;border-radius:6px;
  background:linear-gradient(135deg,#2b4f5e,#6f8f9a 55%,#d9e2e6)}
.hero-arrow{top:300px}
.hero-title{left:806px;top:206px;color:#fff;font-weight:300;font-size:34px;line-height:44px}
.hero-title strong{display:block;font-weight:700;font-size:44px;line-height:54px}
.hero-title strong em{font-style:normal;color:var(--orange)}
.hero-text{left:806px;top:322px;width:320px;color:#d8e6ea;font-size:13.5px;line-height:25px}
.btn{background:var(--orange);color:#fff;font-size:14px;display:flex;align-items:center;justify-content:center}
.hero-btn{left:807px;top:435px;width:131px;height:40px}

/* headings */
.sec-title{font-size:26px;font-weight:400;color:var(--blue)}
.sec-title b{font-weight:700}
.center{left:0;width:1200px;text-align:center}
.sub{color:var(--muted);font-size:13.5px;line-height:22px}

/* services */
.services{left:0;top:606px;width:1200px;height:385px;background:var(--soft)}
.service{width:310px}
.service-icon{width:84px;height:84px;border-radius:50%;display:flex;align-items:center;justify-content:center}
.service h3{position:absolute;left:107px;top:-10px;width:200px;font-size:14px;font-weight:400;line-height:23px}
.service p{position:absolute;left:107px;top:34px;width:215px;font-size:11.5px;line-height:22px;color:var(--muted)}
.service .more{position:absolute;left:107px;top:112px;font-size:11px;white-space:nowrap}

/* testimonials */
.quote-box{left:97px;top:1108px;width:483px;height:290px;border:2px solid var(--line);background:#fff}
.quote-tail{left:520px;top:1396px}
.quote-box p{position:absolute;left:28px;width:430px;font-size:11.5px;line-height:19.5px;color:var(--muted)}
.client{left:251px;top:1160px;font-size:12px;color:var(--muted)}
.client b{color:var(--blue)}
.news-item{left:666px;width:435px;height:111px}
.news-thumb{position:absolute;left:0;top:0;width:80px;height:80px;border-radius:50%}
.news-item p{position:absolute;left:105px;top:4px;width:330px;font-size:11.5px;line-height:21px;color:var(--ink)}
.news-item .date{position:absolute;left:105px;top:51px;font-size:10px;font-weight:700;color:var(--orange);text-transform:uppercase}
.rule{height:1px;background:var(--line)}

/* supporters */
.tile{width:187px;height:84px;border:2px solid var(--line);display:flex;align-items:center;justify-content:center;background:#fff}
.tile span{width:104px;height:30px;border-radius:4px;background:#dcdcdc}

/* about */
.about{left:0;top:1945px;width:1200px;height:496px;background:var(--soft)}
.about-text{left:97px;width:450px;font-size:12px;line-height:23.5px;color:var(--muted)}
.about-media{left:609px;top:2037px;width:492px;height:303px;border-radius:4px;
  background:linear-gradient(180deg,#1d3656,#4a7db0 45%,#9fd8ec 55%,#2a4a6b)}

/* footer */
.foot-h{font-size:13px;color:var(--ink);text-transform:uppercase}
.field{border:1px solid var(--line);background:#fff;font-size:10.5px;color:#aaa;padding:8px 10px;font-style:italic}
.contact-label{font-size:14px;color:var(--orange)}
.contact-val{font-size:12px;color:var(--muted)}
.foot-links{left:97px;top:2702px;font-size:11px;color:var(--ink);text-transform:uppercase;word-spacing:2px}
.copy{left:600px;width:501px;top:2702px;text-align:right;font-size:11px;color:var(--ink);text-transform:uppercase}
</style>
</head>
<body>

<header class="hero">
  <div class="abs brand"><span class="brand-dot"></span>Korvath Bridge</div>
  <nav class="abs nav">
    <svg width="18" height="16" viewBox="0 0 18 16" style="margin-right:30px"><path d="M9 0 18 8h-3v8h-4v-5H7v5H3V8H0z" fill="var(--orange)"/></svg>
    <a>About Us</a><a>Services</a><a>Blog</a><a>Testimonials</a><a>Contact Us</a>
  </nav>
  <div class="abs social"><span style="background:#3b5998"></span><span style="background:#1da1f2"></span><span style="background:var(--red)"></span></div>
  <svg class="abs hero-arrow" style="left:40px" width="24" height="80" viewBox="0 0 24 80"><path d="M22 2 2 40l20 38" fill="none" stroke="#9fb7bd" stroke-width="2"/></svg>
  <svg class="abs hero-arrow" style="left:1136px" width="24" height="80" viewBox="0 0 24 80"><path d="M2 2l20 38L2 78" fill="none" stroke="#9fb7bd" stroke-width="2"/></svg>
  <div class="abs hero-media" role="img" aria-label="Laptop, tablet and phone showing the Korvath Bridge website"></div>
  <h1 class="abs hero-title">Our Customer<strong>SUPPORT <em>KB</em></strong></h1>
  <p class="abs hero-text">Sed ut perspiciatis unde omnis iste luptatem accusantium doloremque laudantium, totam rem aperiam, eaque ipsa quae ab...</p>
  <a class="abs btn hero-btn">Sign Up Today</a>
</header>

<section class="abs services">
  <h2 class="abs center sec-title" style="top:60px"><span style="font-weight:300">Our</span> <b>Services</b></h2>
  <p class="abs center sub" style="top:100px">Sed ut perspiciatis unde omnis iste natus error sit voluptatem accusantium doloremque</p>

  <div class="abs service" style="left:97px;top:159px">
    <div class="service-icon" style="background:var(--blue)"><svg width="44" height="38" viewBox="0 0 44 38"><path d="M12 30H9a8 8 0 0 1 0-16 12 12 0 0 1 23-3 9 9 0 0 1 3 19h-3M22 34V18m-6 6 6-6 6 6" fill="none" stroke="#fff" stroke-width="2.4"/></svg></div>
    <h3 style="color:var(--blue)">Nemo enim ipsam voluptatem</h3>
    <p>Sed ut perspiciatis unde omnis error sit voluptatem accusantium doloremque laudantium, totam rem...</p>
    <a class="more" style="color:var(--blue)">Read More &gt;&gt;</a>
  </div>
  <div class="abs service" style="left:444px;top:159px">
    <div class="service-icon" style="background:var(--orange)"><svg width="44" height="38" viewBox="0 0 44 38"><rect x="4" y="3" width="36" height="26" fill="none" stroke="#fff" stroke-width="2.4"/><path d="M9 23l9-8 6 5 11-11M2 34h40" fill="none" stroke="#fff" stroke-width="2.4"/></svg></div>
    <h3 style="color:var(--orange)">Nemo enim ipsam voluptatem</h3>
    <p>Sed ut perspiciatis unde omnis error sit voluptatem accusantium doloremque laudantium, totam rem...</p>
    <a class="more" style="color:var(--orange)">Read More &gt;&gt;</a>
  </div>
  <div class="abs service" style="left:793px;top:159px">
    <div class="service-icon" style="background:var(--green)"><svg width="44" height="40" viewBox="0 0 44 40"><circle cx="16" cy="22" r="9" fill="none" stroke="#fff" stroke-width="2.4" stroke-dasharray="4 2"/><circle cx="16" cy="22" r="4" fill="none" stroke="#fff" stroke-width="2.4"/><circle cx="32" cy="10" r="6" fill="none" stroke="#fff" stroke-width="2.4" stroke-dasharray="3 2"/></svg></div>
    <h3 style="color:var(--green)">Nemo enim ipsam voluptatem</h3>
    <p>Sed ut perspiciatis unde omnis error sit voluptatem accusantium doloremque laudantium, totam rem...</p>
    <a class="more" style="color:var(--green)">Read More &gt;&gt;</a>
  </div>
</section>

<h2 class="abs sec-title" style="left:97px;top:1046px"><span style="font-weight:400">Client</span> <b>Testimonials</b></h2>
<div class="abs quote-box">
  <p style="top:114px">Nemo enim ipsam voluptatem quia voluptas sit aspernatur aut odit aut fugit, sed quia consequuntur magni dolores eos qui ratione voluptatem sequi nesciunt. Neque porro quia non numquam numquam eius modi...</p>
  <p style="top:194px">Consequuntur magni dolores eos qui ratione voluptatem sequi nesciunt. Neque porro quisquam est, qui dolorem ipsum quia dolor sit amet, consectetur, adipisci velit, sed quia non numquam numquam eius modi...</p>
</div>
<svg class="abs quote-tail" width="30" height="28" viewBox="0 0 30 28"><path d="M1 1v26L29 1" fill="#fff" stroke="var(--line)" stroke-width="2"/></svg>
<svg class="abs" style="left:125px;top:1140px" width="60" height="60" viewBox="0 0 60 60"><circle cx="29" cy="29" r="29" fill="var(--blue)"/><path d="M16 34c0-8 3-12 9-14v4c-3 1-4 3-4 5h4v8h-9zm14 0c0-8 3-12 9-14v4c-3 1-4 3-4 5h4v8h-9z" fill="#fff"/></svg>
<div class="abs" role="img" aria-label="Client portrait" style="left:169px;top:1140px;width:58px;height:58px;border-radius:50%;background:linear-gradient(180deg,#c9ced3,#6b737b);border:3px solid #fff"></div>
<div class="abs client"><b>-MARTIN OSVALD</b> / Our Client</div>
<div class="abs" style="left:528px;top:1158px;font-size:14px;color:#aaa">&lsaquo; &rsaquo;</div>

<h2 class="abs sec-title" style="left:666px;top:1046px"><span style="font-weight:400">Recent</span> <b>News</b></h2>
<div class="abs news-item" style="top:1110px">
  <div class="news-thumb" role="img" aria-label="Cloud computing news photo" style="background:linear-gradient(135deg,#cfe8f7,#2f7fc0)"></div>
  <p>Nemo enim ipsam voluptatem quia voluptas sit aspernatur aut odit aut fugit, sed quia consequuntur...</p>
  <span class="date">Posted on October 23,2016</span>
</div>
<div class="abs rule" style="left:666px;top:1205px;width:435px"></div>
<div class="abs news-item" style="top:1222px">
  <div class="news-thumb" role="img" aria-label="Circuit board news photo" style="background:linear-gradient(135deg,#3b6fd0,#0d2a6b)"></div>
  <p>Nemo enim ipsam voluptatem quia voluptas sit aspernatur aut odit aut fugit, sed quia consequuntur...</p>
  <span class="date">Posted on October 23,2016</span>
</div>
<div class="abs rule" style="left:666px;top:1316px;width:435px"></div>
<div class="abs news-item" style="top:1333px">
  <div class="news-thumb" role="img" aria-label="Cloud download news photo" style="background:linear-gradient(135deg,#5a6470,#111820)"></div>
  <p>Nemo enim ipsam voluptatem quia voluptas sit aspernatur aut odit aut fugit, sed quia consequuntur...</p>
  <span class="date">Posted on October 23,2016</span>
</div>

<div class="abs rule" style="left:0;top:1490px;width:1200px"></div>
<h2 class="abs center sec-title" style="top:1553px"><span style="font-weight:400">Our</span> <b>Supporters</b></h2>
<p class="abs center sub" style="top:1600px">Sed ut perspiciatis unde omnis iste natus error sit voluptatem accusantium doloremque laudantium,<br>totam eaque ipsa quae ab illo inventore veritatis</p>
<div class="abs tile" style="left:97px;top:1679px"><span></span></div>
<div class="abs tile" style="left:301px;top:1679px"><span></span></div>
<div class="abs tile" style="left:506px;top:1679px"><span></span></div>
<div class="abs tile" style="left:710px;top:1679px"><span></span></div>
<div class="abs tile" style="left:914px;top:1679px"><span></span></div>
<div class="abs tile" style="left:97px;top:1781px"><span></span></div>
<div class="abs tile" style="left:301px;top:1781px"><span></span></div>
<div class="abs tile" style="left:506px;top:1781px"><span></span></div>
<div class="abs tile" style="left:710px;top:1781px"><span></span></div>
<div class="abs tile" style="left:914px;top:1781px"><span></span></div>

<section class="abs about">
  <h2 class="abs sec-title" style="left:97px;top:82px"><span style="font-weight:400">About</span> <b>Korvath Bridge LLC</b></h2>
</section>
<p class="abs about-text" style="top:2077px">Sed ut perspiciatis unde omnis iste natus error sit voluptatem doloremquetium, totam vitae dicta sunt explicabo. Nemo enim ipsam voluptatem quia voluptas sit aspernatur aut odit aut fugit, sed quia consequuntur magni dolores eos qui ratione voluptatem sequi nesciunt. Neque porro quisquam est, qui dolorem...</p>
<p class="abs about-text" style="top:2184px">Sed ut perspiciatis unde omnis iste natus error sit voluptatem doloremquetium, totam vitae dicta sunt explicabo. Nemo enim ipsam voluptatem quia voluptas sit aspernatur aut odit aut fugit, sed quia consequuntur magni dolores eos qui ratione voluptatem sequi nesciunt. Neque porro quisquam est, qui dolorem...</p>
<a class="abs btn" style="left:99px;top:2303px;width:129px;height:40px">Read More Info</a>
<div class="abs about-media" role="img" aria-label="Data centre server room corridor"></div>

<footer>
  <h4 class="abs foot-h" style="left:97px;top:2488px">Newsletter</h4>
  <div class="abs field" style="left:97px;top:2532px;width:266px;height:39px">name ...</div>
  <div class="abs field" style="left:97px;top:2586px;width:266px;height:38px">email ...</div>
  <div class="abs field" style="left:378px;top:2532px;width:268px;height:92px">your query ...</div>
  <a class="abs btn" style="left:659px;top:2587px;width:73px;height:37px">Send</a>
  <div class="abs" style="left:765px;top:2523px;width:1px;height:105px;background:var(--line)"></div>

  <h4 class="abs foot-h" style="left:795px;top:2488px">Contact Info</h4>
  <svg class="abs" style="left:794px;top:2535px" width="24" height="22" viewBox="0 0 24 22"><path d="M12 0 24 11h-4v11h-5v-7H9v7H4V11H0z" fill="var(--orange)"/></svg>
  <div class="abs contact-label" style="left:829px;top:2529px">Address</div>
  <div class="abs contact-val" style="left:829px;top:2551px">some block, steet number, city name,</div>
  <svg class="abs" style="left:794px;top:2583px" width="20" height="22" viewBox="0 0 20 22"><rect width="20" height="22" rx="3" fill="var(--orange)"/><path d="M6 5c0 7 3 11 9 12l1-3-3-1-1 1c-2-1-3-3-4-5l1-1-1-3z" fill="#fff"/></svg>
  <div class="abs contact-label" style="left:829px;top:2578px">Phone</div>
  <div class="abs contact-val" style="left:829px;top:2599px">(000) 555 014 2200</div>
  <svg class="abs" style="left:956px;top:2585px" width="22" height="16" viewBox="0 0 22 16"><rect width="22" height="16" fill="var(--orange)"/><path d="M1 1l10 8 10-8" fill="none" stroke="#fff" stroke-width="2"/></svg>
  <div class="abs contact-label" style="left:991px;top:2578px">Email us</div>
  <div class="abs contact-val" style="left:991px;top:2599px">hello@korvathbridge.com</div>

  <div class="abs rule" style="left:97px;top:2670px;width:1004px"></div>
  <div class="abs foot-links">Home &nbsp;|&nbsp; About Us &nbsp;|&nbsp; Services &nbsp;|&nbsp; Blog &nbsp;|&nbsp; Testimonials &nbsp;|&nbsp; Contact Us</div>
  <div class="abs copy">Copyrights © 2016 . Korvath Bridge LLC | Allrights Reserved.</div>
</footer>

</body>
</html>
```